Eco friendly Swedish beauty products sold in aluminum bottles - label design needed

We need help in designing a series of stick on labels for 80 ml (2.7 fl. oz.) aluminum bottles containing beauty products such as soaps, shampoo etc. The diameter of the bottle is 36 mm and the body of the bottles measures approx. 106 mm.
It is important for us that the label has a simplistic and clean feel with few colors (and the right ones!) and that the label helps amplify this product being both better and a more sustainable alternative to many of our plastic bottle competitors. The design and label should communicate the feel of an Eco-friendly, sustainable and modern brand of high quality - and with a Swedish concept.
We are using Montserrat font in our materials. Find attached information of preferred colors, the bottles and one example of our logotype. I am also available on e-mail should further information be needed.

Looking forward and very excited to receive your suggestions.
Note that we are expecting to start selling a series of approximately 10 different products where I will need one "master design" and then only smaller changes for each of the different products.

Target Market(s)

People whom are aware and not only look at price tag. Private and commercial market.

Industry/Entity Type

Beauty

Font styles to use
Other font styles liked:
• Montserrat

Requirements
Must have
• It must give the feel of being both better and a more sustainable alternative to many of our plastic bottle competitors.
Nice to have
• Simplistic. Clean. Clear.
Should not have
• Wrong colors, too complex designs.

```html
<!DOCTYPE html>
<html lang="en">
<head>
<meta charset="utf-8">
<title>Mosslyn Bath – Shampoo Label</title>
<link href="https://fonts.googleapis.com/css2?family=Montserrat:wght@400;500;700&family=Sacramento&display=swap" rel="stylesheet">
<style>
  :root {
    --canvas: #ffffff;
    --label: #e0dedb;
    --label-shade: #d3d0cb;
    --green-dark: #3e4a16;
    --green-olive: #6f8040;
    --green-soft: #8a9a62;
    --ink: #1d1d1b;
  }
  html, body {
    margin: 0;
    width: 1200px;
    height: 1200px;
    overflow: hidden;
    background: var(--canvas);
  }
  .canvas {
    position: relative;
    width: 1200px;
    height: 1200px;
  }
  .label {
    position: absolute;
    left: 338px;
    top: 100px;
    width: 525px;
    height: 1000px;
    background: linear-gradient(90deg, var(--label) 0%, var(--label-shade) 45%, var(--label) 100%);
    overflow: hidden;
    font-family: 'Montserrat', sans-serif;
  }
  .rule-band {
    position: absolute;
    left: 0;
    width: 100%;
    height: 14px;
    background: linear-gradient(180deg, var(--green-soft) 0%, var(--green-dark) 50%, var(--green-soft) 100%);
  }
  .rule-band--top { top: 30px; }
  .rule-band--bottom { top: 962px; }

  .brand-name {
    position: absolute;
    left: 30px;
    bottom: 79px;
    writing-mode: vertical-rl;
    transform: rotate(180deg);
    font-size: 72px;
    font-weight: 400;
    line-height: 1;
    letter-spacing: 6px;
    color: var(--ink);
    white-space: nowrap;
  }
  .brand-line {
    position: absolute;
    left: 126px;
    bottom: 700px;
    writing-mode: vertical-rl;
    transform: rotate(180deg);
    font-size: 24px;
    font-weight: 500;
    letter-spacing: 11px;
    line-height: 1;
    color: var(--ink);
    white-space: nowrap;
  }
  .accent-bar {
    position: absolute;
    left: 126px;
    top: 330px;
    width: 22px;
    height: 590px;
    background: var(--green-soft);
  }
  .product-name {
    position: absolute;
    left: 174px;
    top: 570px;
    margin: 0;
    font-size: 60px;
    font-weight: 700;
    letter-spacing: 0.5px;
    line-height: 1;
    color: var(--green-olive);
  }
  .divider-dots {
    position: absolute;
    left: 363px;
    top: 663px;
    display: flex;
    gap: 5px;
  }
  .divider-dots span {
    width: 7px;
    height: 7px;
    border-radius: 50%;
    background: var(--green-dark);
  }
  .tagline {
    position: absolute;
    left: 170px;
    top: 730px;
    font-family: 'Sacramento', cursive;
    font-size: 46px;
    line-height: 1;
    color: var(--green-olive);
    white-space: nowrap;
  }
  .hair-type {
    position: absolute;
    left: 178px;
    top: 800px;
    width: 342px;
    height: 56px;
    border-top: 2px solid var(--green-olive);
    border-bottom: 2px solid var(--green-olive);
    box-sizing: border-box;
    display: flex;
    align-items: center;
    justify-content: center;
    font-size: 23px;
    font-weight: 500;
    letter-spacing: 2px;
    color: var(--green-dark);
  }
  .volume {
    position: absolute;
    left: 172px;
    top: 890px;
    font-size: 24px;
    font-weight: 400;
    color: var(--green-dark);
  }
</style>
</head>
<body>
<main class="canvas">
  <section class="label">
    <div class="rule-band rule-band--top"></div>

    <div class="brand-name">MOSSLYN BATH</div>
    <div class="brand-line">NORDIC</div>
    <div class="accent-bar"></div>

    <h1 class="product-name">SHAMPOO</h1>
    <div class="divider-dots"><span></span><span></span><span></span></div>
    <div class="tagline">all natural ingredients</div>
    <div class="hair-type">FOR ALL HAIR TYPE</div>
    <div class="volume">200ml</div>

    <div class="rule-band rule-band--bottom"></div>
  </section>
</main>
</body>
</html>
```